Business Cards and Print Material
Business cards and print material
I like something that is out of the box. Something different and memorable. I will also need design for envelopes and letter heads. I like the designs so far. Please keep up the good work!
any info or ideas on what you would like ????

```html
<!DOCTYPE html>
<html lang="en">
<head>
<meta charset="utf-8">
<title>Meridian Scan Group – Business Card</title>
<link href="https://fonts.googleapis.com/css2?family=Carlito:wght@400;700&display=swap" rel="stylesheet">
<style>
  :root {
    --page: #ffffff;
    --card-edge: #8a8a8a;
    --navy: #323466;
    --ink: #34406f;
    --ink-soft: #4b5482;
    --brand-blue: #6f86b8;
    --brand-pale: #c9d3e8;
    --white: #ffffff;
  }
  * { margin: 0; padding: 0; box-sizing: border-box; }
  html, body {
    width: 1200px; height: 869px; overflow: hidden;
    background: var(--page);
    font-family: "Carlito", "Calibri", sans-serif;
  }
  .canvas { position: relative; width: 1200px; height: 869px; }
  .card {
    position: absolute; left: 211px; top: 211px;
    width: 778px; height: 442px;
    border: 1.5px solid var(--card-edge);
    background: var(--white);
  }
  .web-band {
    position: absolute; left: 132px; top: 36px;
    width: 645px; height: 36px;
    background: var(--navy);
    border-top-left-radius: 14px;
    color: var(--white);
    font-size: 23px; line-height: 36px;
    padding-left: 150px;
  }
  .brand {
    position: absolute; left: 40px; top: 100px;
    width: 336px; height: 216px;
    display: flex; flex-direction: column; align-items: center; justify-content: center;
    gap: 14px;
  }
  .brand-dot {
    width: 70px; height: 70px; border-radius: 50%;
    background: linear-gradient(180deg, var(--brand-pale), var(--brand-blue));
  }
  .brand-name {
    color: var(--brand-blue);
    font-size: 30px; letter-spacing: 2px;
    text-transform: uppercase; text-align: center; line-height: 1.1;
  }
  .person { position: absolute; left: 432px; top: 116px; color: var(--ink); }
  .person-name { font-size: 40px; line-height: 1; text-transform: uppercase; }
  .person-title { font-size: 20px; margin-top: 4px; text-transform: uppercase; }
  .contacts { position: absolute; left: 432px; top: 188px; color: var(--ink-soft); font-size: 22px; line-height: 29px; list-style: none; }
  .address { position: absolute; left: 39px; top: 334px; color: var(--navy); font-size: 23px; }
  .mail-band {
    position: absolute; left: 0; top: 372px;
    width: 581px; height: 36px;
    background: var(--navy);
    border-top-right-radius: 16px; border-bottom-right-radius: 16px;
    color: var(--white); font-size: 23px; line-height: 36px;
    padding-left: 39px;
  }
</style>
</head>
<body>
<div class="canvas">
  <div class="card">
    <div class="web-band">www.meridianscangroup.com</div>
    <div class="brand">
      <div class="brand-dot"></div>
      <div class="brand-name">Meridian Scan Group</div>
    </div>
    <div class="person">
      <div class="person-name">Tessa Wilde</div>
      <div class="person-title">Director of Operations</div>
    </div>
    <ul class="contacts">
      <li>Toll free: 1800.555.0142</li>
      <li>Phone: 210.555.0187</li>
      <li>Cell: 210.555.0163</li>
      <li>Fax: 210.555.0129</li>
    </ul>
    <div class="address">15420 Cedar Ridge Pkwy, Suite 204-112, San Antonio, TX 78232</div>
    <div class="mail-band">E-mail: tessa@meridianscangroup.com</div>
  </div>
</div>
</body>
</html>
```